Dietetic office: Bright Meal

I want to give my business card a modern and warm look (which attracts the eye and has a reassuring side), which links dietetics to a moment of well-being. The front and back sides must be used (not just to put the logo on the front side)

The map should be eye-catching and easy to read. I don't necessarily want to have a plain background, which I find visually weighs down the maps.
I really like the square format of a business card with rounded edges which is different from what we are used to finding (and why not take this square diagonally?), however I am not closed to another format as long as I like the style.

Who am I? Coraline, 32 years old, Dietician and passionate about food since always. I am specialized in slimming and an expert in micro nutrition, which means that I take into account not only the nutritional balance while maintaining pleasure (if foods are present in the business card, I do not want some cliché things where there would just be fruits and vegetables, but really something more global), but also the psycho-emotional dimension that I will treat with food supplements based on plants, fruits or vegetables.

-----------------------------------------------------------------------------------

 Mention to appear on the card IN FRENCH (please be careful in case of translation that the use of words is correct):

Coraline MAUREL
Dietician Nutritionist
Expert in Slimming and Micro-Nutrition

Slogan: I help you lose weight sustainably with pleasure and by reconciling your events

Catchphrases: Want to lose weight? Do you like going out? Do you have a lot of events? And is pleasure on your plate important to you?

Make an appointment on Rendivo or on 06 41 83 52 17
coraline.brightmeal@exemplonet.fr
Address: Health Center, Allée des Glycines, 13492 Vitrolles
www.brightmeal-exemple.fr
Chatterbook + Picturegram Logo

- The company logo has been uploaded for your viewing. Other file formats can be made available if required.
- I would like a place for a photo of me to be possible.
Updates

Good morning,
I want to have a business card that is both lively and warm. Which will easily catch the eye while being easy to read and make people understand that I am in the field of well-being.
I like the square side in business cards (and why not use them diagonally?), or a more classic but original one.
Both the front and back sides must be used (I don't want to have the logo on just one side)
I don't want to have a plain background, but rather something more muted (I really like the suggestion from "Pine Kettle Graphic Designer" for this)
the use of logo for telephone, mail, address, rendivo, chatterbook, picto etc is possible in order to facilitate reading

Please follow the various elements of the brief regarding the text and use the French text as it is.

I like business cards preferably square (with the possibility of using them diagonally).
The map should be eye-catching and easy to read.
It must bring pep while having softness which brings back to the well-being side
The card must be used on the front and back for the different elements (I do not want to have only the logo on the front side)
The text must correspond to the brief (be careful with the translation which can sometimes be bad)
I don't want to have a plain blue or orange background. I really like the idea of the background from "Pine Kettle Graphic Designer"

You can if you wish use symbols for contacts, telephone, rendivo, address, cb, picto....

Target Market(s)

mainly women between 25 and 65 years old + men around 40 years old

Contact Information for Business Card

22

Font styles to use
Sans Serif
Script

Colors
0054AA
0677BA
7BADD7
CADEEF
E8F1F8
0094D4
00A9DD
6FCCEA
C7EBF8
E9F6FB
00AB8E
00BBA5
67D7C9
C6EFE9
E9F9F6
FFC000
F8CF3A
FAE287
FDF2CF
FEFAEE
F0912C
F2A743
F7CA91
FBE8D2
FDF5EE

Requirements
Must have
• some pep! while being refined
Nice to have
• I really like the square format of a business card with rounded edges which is different from what we are used to finding, however I am not closed to another format as long as I like the style.
Should not have
• if foods are represented, only show fruits and vegetables (too cliché)

```html
<!DOCTYPE html>
<html lang="fr">
<head>
<meta charset="utf-8">
<title>Bright Meal – cartes de visite</title>
<link href="https://fonts.googleapis.com/css2?family=Martel:wght@300;400&family=Patrick+Hand&display=swap" rel="stylesheet">
<style>
  :root{
    --stage:#1d3a32;
    --terracotta:#cf6650;
    --terracotta-deep:#b9503c;
    --orange-line:#f2a743;
    --cream:#f7f5e7;
    --white:#ffffff;
    --ink:#1f3a33;
    --apple:#d3262b;
    --carrot:#c9382c;
    --avocado:#e4e8c8;
  }
  html,body{margin:0;padding:0;width:1200px;height:900px;overflow:hidden;background:var(--stage);}
  .stage{position:relative;width:1200px;height:900px;}
  .card{position:absolute;top:254px;width:450px;height:450px;transform:scale(.873);transform-origin:top left;overflow:hidden;background:var(--white);}
  .card--front{left:180px;}
  .card--back{left:628px;}
  .card__bg{position:absolute;inset:0;width:450px;height:450px;}
  .t{position:absolute;margin:0;white-space:nowrap;color:var(--terracotta);}
  .script{font-family:"Patrick Hand",cursive;}
  .serif{font-family:"Martel",serif;font-weight:300;}
  .question{font-size:21px;left:0;width:444px;text-align:center;}
  .brand{font-family:"Martel",serif;font-weight:400;color:var(--ink);display:flex;align-items:center;gap:6px;}
  .brand__dot{width:10px;height:10px;border-radius:50%;background:var(--terracotta);}
  .icon{position:absolute;}
  .booking{position:absolute;right:22px;top:310px;display:flex;flex-direction:column;align-items:flex-end;gap:2px;}
  .booking__phone{display:flex;align-items:center;gap:8px;font-family:"Patrick Hand",cursive;font-size:27px;color:var(--terracotta);}
  .booking__label{font-family:"Martel",serif;font-weight:300;font-size:15px;color:var(--terracotta);}
  .channels{display:flex;gap:8px;font-family:"Martel",serif;font-weight:400;font-size:11px;color:var(--terracotta);margin-top:4px;}
  .channels span{display:flex;align-items:center;gap:3px;}
  .channels i{width:7px;height:7px;border-radius:2px;background:var(--terracotta);display:inline-block;}
</style>
</head>
<body>
<main class="stage">

  <!-- Recto -->
  <section class="card card--front">
    <svg class="card__bg" viewBox="0 0 450 450">
      <rect width="450" height="225" fill="var(--terracotta)"/>
      <rect y="225" width="450" height="225" fill="var(--cream)"/>
      <path d="M160,0 C140,20 130,60 135,85 C140,110 110,112 70,118 C25,128 30,170 40,215 C52,265 15,300 10,350 C5,410 40,440 70,450" fill="none" stroke="var(--orange-line)" stroke-width="2"/>
      <path d="M150,0 L330,0 C350,20 345,70 360,95 C380,125 440,105 442,150 C444,200 405,210 410,250 C415,300 450,320 440,370 C430,420 400,440 380,450 L60,450 C30,430 10,400 20,350 C30,300 60,270 45,220 C35,170 20,130 60,115 C100,105 125,110 120,70 C115,35 125,15 150,0 Z" fill="var(--white)"/>
      <path d="M260,0 C320,5 360,20 365,70 C370,110 400,105 440,110 C455,140 450,180 430,220 C420,260 440,300 450,320" fill="none" stroke="var(--orange-line)" stroke-width="2"/>
      <ellipse cx="325" cy="285" rx="25" ry="28" fill="var(--cream)" role="img" aria-label="Pomme en filigrane"/>
      <rect x="190" y="380" width="22" height="80" rx="10" transform="rotate(45 200 420)" fill="var(--cream)" role="img" aria-label="Carotte en filigrane"/>
      <g role="img" aria-label="Illustration de pomme">
        <ellipse cx="401" cy="42" rx="25" ry="30" fill="var(--apple)"/>
      </g>
      <g role="img" aria-label="Illustration de carotte">
        <rect x="48" y="30" width="22" height="85" rx="10" transform="rotate(35 59 72)" fill="var(--carrot)"/>
      </g>
      <g role="img" aria-label="Illustration d'avocat">
        <ellipse cx="392" cy="184" rx="18" ry="26" transform="rotate(-25 392 184)" fill="var(--avocado)"/>
      </g>
    </svg>

    <p class="t script question" style="top:66px">Aimez-vous sortir?</p>
    <p class="t script question" style="top:113px">Vous voulez perdre du poids ?</p>
    <p class="t script question" style="top:160px;line-height:28px">Et le plaisir dans votre assiette<br>est-il important pour vous ?</p>
    <p class="t script question" style="top:235px">Avez-vous beaucoup d'événements?</p>

    <div class="t brand" style="left:24px;top:334px;font-size:26px"><span class="brand__dot"></span>Bright Meal</div>

    <div class="booking">
      <div class="booking__phone">
        <svg width="18" height="18" viewBox="0 0 24 24"><path d="M6.6 10.8a15 15 0 0 0 6.6 6.6l2.2-2.2a1 1 0 0 1 1-.25 11.4 11.4 0 0 0 3.6.57 1 1 0 0 1 1 1V20a1 1 0 0 1-1 1A17 17 0 0 1 3 4a1 1 0 0 1 1-1h3.5a1 1 0 0 1 1 1c0 1.25.2 2.45.57 3.6a1 1 0 0 1-.25 1z" fill="none" stroke="var(--terracotta)" stroke-width="2"/></svg>
        <span>413-555-0172</span>
      </div>
      <span class="booking__label">Prendre rendez-vous sur</span>
      <div class="channels">
        <span><i></i>Rendivo</span>
        <span><i></i>Picturegram</span>
        <span><i></i>Chatterbook</span>
      </div>
    </div>
  </section>

  <!-- Verso -->
  <section class="card card--back">
    <svg class="card__bg" viewBox="0 0 450 450">
      <rect width="450" height="450" fill="var(--terracotta)"/>
      <path d="M0,0 L180,0 C260,0 315,10 330,40 C342,70 345,105 385,118 C430,135 440,160 420,200 C400,230 350,220 360,250 C370,290 430,300 450,330 L450,450 L0,450 Z" fill="var(--white)"/>
      <path d="M230,0 C300,10 345,25 352,62 C358,95 365,102 405,108 C448,116 455,160 440,200 C425,235 380,225 385,255 C390,285 440,295 450,300" fill="none" stroke="var(--orange-line)" stroke-width="2"/>
      <g role="img" aria-label="Illustration de pomme">
        <ellipse cx="368" cy="50" rx="25" ry="30" fill="var(--apple)"/>
      </g>
      <g role="img" aria-label="Illustration de carotte">
        <rect x="408" y="25" width="20" height="80" rx="9" transform="rotate(15 418 65)" fill="var(--terracotta-deep)"/>
      </g>
      <g role="img" aria-label="Illustration d'avocat">
        <ellipse cx="385" cy="172" rx="16" ry="23" transform="rotate(-25 385 172)" fill="var(--avocado)"/>
      </g>
    </svg>

    <p class="t serif" style="left:20px;top:38px;font-size:28px;font-weight:400">Coraline MAUREL</p>
    <p class="t serif" style="left:33px;top:80px;font-size:18px">Diététicienne Nutritionniste</p>
    <p class="t serif" style="left:33px;top:111px;font-size:18px">Expert en Minceur et Micro-Nutrition</p>

    <svg class="icon" style="left:33px;top:161px" width="14" height="14" viewBox="0 0 24 24"><rect x="3" y="5" width="18" height="14" rx="1" fill="none" stroke="var(--terracotta)" stroke-width="2"/><path d="M3 6l9 7 9-7" fill="none" stroke="var(--terracotta)" stroke-width="2"/></svg>
    <p class="t serif" style="left:56px;top:153px;font-size:15px">coraline.brightmeal@exemplonet.fr</p>
    <svg class="icon" style="left:33px;top:193px" width="14" height="14" viewBox="0 0 24 24"><circle cx="12" cy="12" r="9" fill="none" stroke="var(--terracotta)" stroke-width="2"/><path d="M3 12h18M12 3c3 3 3 15 0 18M12 3c-3 3-3 15 0 18" fill="none" stroke="var(--terracotta)" stroke-width="2"/></svg>
    <p class="t serif" style="left:56px;top:184px;font-size:16px">www.brightmeal-exemple.fr</p>

    <svg class="icon" style="left:32px;top:248px" width="14" height="18" viewBox="0 0 24 30"><path d="M12 0a10 10 0 0 0-10 10c0 8 10 19 10 19s10-11 10-19A10 10 0 0 0 12 0z" fill="var(--terracotta)"/><circle cx="12" cy="10" r="4" fill="var(--white)"/></svg>
    <p class="t serif" style="left:56px;top:242px;font-size:17px;line-height:31px">18 North Orchard Ln<br>Lenox Hollow,<br>MA 01299</p>

    <div class="t brand" style="left:246px;top:277px;font-size:21px"><span class="brand__dot" style="width:8px;height:8px"></span>Bright Meal</div>

    <p class="t script" style="left:0;width:450px;text-align:center;top:365px;font-size:19px;line-height:27px">Je vous aide à perdre du poids durablement avec<br>plaisir et en conciliant vos événements</p>
  </section>

</main>
</body>
</html>
```